Homepage für Immobilienmakler
Zielgruppe
Wir sind ein neuer und junger Immobilienmakler. Wir wollen moderne und neue Wege gehen. Damit meinen wir, extrem modern und auffallend professionell.
Unsere Immobilien sind von Anlegerwohnungen über Häuser bis hin zu Gewerbeimmobilien
Unsere Zielgruppe ist von jung bis alt quer durch.
Aufgabenstellung
Homepagegestalltung für unsere Immobilienmaklerei.
Persönlich gefällt mir sehr gut das schwarz-weiß, jedoch wirkt das dann eher zu dunkel nehme ich mal an. Sonst würde mir die Homepage in grün, wie die Farbe im Logo, gut gefallen. Eventuell in weißer Schrift. ABER, ICH ÜBERLASSE EUCH DIE DESIGNSFARBEN.
Mir hätte dieses Design sehr gut gefallen, eventuelll könnt ihr dieses umgestallten:
http://vorlagenhain.example/item/auto-dealer-car-dealer-html-template/full_screen_preview/7719034
Kein muss, wenn ihr etwas besseres habt, dann bin ich auch froh ;)
Eventuell etwas mit Bewegung auf der Homepage oder so wäre auch gut.
Unsere Homepage hat die Domain:
wohnraum-kontor.example
Das Foto von mir sollte auf der Homepage eingebaut werden.
Auf der Homepage sollen die Immobilien, die wir verkaufen und vermieten angeführt werden. Zudem sollte ersichtlich sein, dass wir Immobilien suchen, um diese zu verkaufen oder zu vermieten.

```html
<!DOCTYPE html>
<html lang="de">
<head>
<meta charset="utf-8">
<title>Wohnraum Kontor – Immobilien</title>
<link rel="stylesheet" href="https://fonts.googleapis.com/css2?family=Arimo:wght@400;700&display=swap">
<style>
  :root{
    --black:#000;
    --ink:#2b2b2b;
    --green:#8cc63f;
    --grey-band:#e4e4e4;
    --grey-box:#e6e6e6;
    --grey-line:#c8c8c8;
    --caption:#1e1e1e;
    --white:#fff;
    --btn:#8a8a8a;
  }
  *{box-sizing:border-box;margin:0;padding:0}
  html,body{width:972px;height:1200px;overflow:hidden;background:var(--white)}
  body{position:relative;font-family:"Arimo",Arial,sans-serif;color:var(--ink)}
  .abs{position:absolute}

  .site-header{left:0;top:0;width:972px;height:142px;background:var(--black)}
  .agent-photo{left:81px;top:8px;width:62px;height:134px;background:linear-gradient(#3a3a3a,#d8d8d8 45%,#1a1a1a);border-radius:28px 28px 4px 4px}
  .brand{left:171px;top:14px;display:flex;align-items:center;gap:10px}
  .brand-name{font-size:44px;font-weight:700;color:var(--green);letter-spacing:-1px}
  .brand-dot{width:14px;height:14px;border-radius:50%;background:var(--green)}
  .social{left:824px;top:18px;display:flex;gap:10px}
  .social span{width:16px;height:16px;background:#d9d9d9}

  .main-nav{left:0;top:142px;width:972px;height:35px;background:var(--grey-band)}
  .main-nav a{position:absolute;top:10px;font-size:14px;font-weight:700;color:var(--ink);text-decoration:none}

  .section-title{left:79px;font-size:18px;font-weight:700;width:815px;padding-bottom:8px;border-bottom:1px solid var(--grey-line)}
  .intro{left:79px;top:292px;font-size:12.5px;line-height:19px}

  .feature{left:78px;top:420px;width:342px;height:263px;background:linear-gradient(#8fb4dc,#dfe8ee 40%,#7f9c6a 75%,#bfc6b8)}
  .caption{position:absolute;left:0;bottom:0;width:100%;height:31px;background:var(--caption);color:var(--white);font-size:14px;font-weight:700;display:flex;justify-content:space-between;align-items:center;padding:0 11px}
  .caption .price{color:var(--green)}

  .search{left:440px;top:420px;width:236px;height:263px;background:var(--grey-box);border:1px solid #cfcfcf;padding:14px 11px}
  .search h3{font-size:14px;margin-bottom:16px}
  .select{position:relative;height:22px;background:var(--white);border:1px solid #cfcfcf;font-size:12.5px;color:#999;padding:3px 8px;margin-bottom:18px}
  .select::after{content:"";position:absolute;right:9px;top:8px;border:5px solid transparent;border-top:5px solid #aaa}
  .search-btn{position:absolute;right:14px;top:187px;width:70px;height:21px;background:var(--btn);border:1px solid #6d6d6d;font:700 13px "Arimo",Arial,sans-serif;color:var(--ink)}

  .about{left:696px;top:420px;width:198px;height:263px;background:var(--black);color:var(--white);padding:14px 15px}
  .about h3{font-size:14px;color:var(--green);margin-bottom:14px}
  .about p{font-size:12.5px;line-height:19px}

  .arrows{left:864px;top:721px}
  .listing{top:772px;width:197px;height:149px;background:linear-gradient(#3f6fa8,#b9cde0 45%,#6f8a5c 80%,#4a5a44)}
  .listing .caption{height:35px}

  .site-footer{left:0;top:1031px;width:972px;height:169px;background:var(--grey-band)}
  .footer-col{top:1054px;font-size:12.5px;line-height:19px}
  .footer-col h4{font-size:14px;margin-bottom:12px}
</style>
</head>
<body>
  <header class="abs site-header"></header>
  <div class="abs agent-photo" role="img" aria-label="Foto des Maklers"></div>
  <div class="abs brand"><span class="brand-name">Wohnraum Kontor</span><span class="brand-dot"></span></div>
  <div class="abs social"><span></span><span></span><span></span></div>

  <nav class="abs main-nav">
    <a style="left:80px" href="#">Immobilien Kaufen</a>
    <a style="left:285px" href="#">Immobilien Verkaufen</a>
    <a style="left:490px" href="#">Kontakt</a>
  </nav>

  <h1 class="abs section-title" style="top:245px">Herzlich Willkommen bei Wohnraum Kontor!</h1>
  <p class="abs intro">Sie sind auf der Suche nach preiswerten Immobilien? Dann sind Sie bei uns genau richtig!<br>Sie wollen eine Immobilie verkaufen? Dann kontaktieren Sie uns einfach!</p>

  <h2 class="abs section-title" style="top:366px">Immobilien kaufen</h2>

  <div class="abs feature" role="img" aria-label="Foto eines modernen Einfamilienhauses">
    <div class="caption"><span>Angebot</span><span class="price">Preis</span></div>
  </div>

  <form class="abs search">
    <h3>Immobiliensuche</h3>
    <div class="select">Was</div>
    <div class="select">Wo</div>
    <div class="select">Preis</div>
    <button class="search-btn" type="button">Suche!</button>
  </form>

  <aside class="abs about">
    <h3>Über uns</h3>
    <p>Überall dieselbe alte Leier. Das Layout ist fertig, der Text lässt auf sich warten. Damit das Layout nun nicht nackt im Raume steht und sich klein und leer vorkommt, springe ich ein: der Blindtext.</p>
  </aside>

  <h2 class="abs section-title" style="top:720px">Aktuelle Angebote</h2>
  <svg class="abs arrows" width="30" height="18" viewBox="0 0 30 18" aria-hidden="true">
    <path d="M10 0 L1 9 L10 18 Z" fill="#555"/><path d="M18 0 L27 9 L18 18 Z" fill="#555"/>
  </svg>

  <div class="abs listing" style="left:79px" role="img" aria-label="Foto einer modernen Villa mit Pool"><div class="caption"><span>Angebot</span><span class="price">Preis</span></div></div>
  <div class="abs listing" style="left:284px" role="img" aria-label="Foto eines weißen Bauhaus-Hauses"><div class="caption"><span>Angebot</span><span class="price">Preis</span></div></div>
  <div class="abs listing" style="left:489px" role="img" aria-label="Foto eines Hauses mit Balkon"><div class="caption"><span>Angebot</span><span class="price">Preis</span></div></div>
  <div class="abs listing" style="left:694px" role="img" aria-label="Foto eines Einfamilienhauses mit Solardach"><div class="caption"><span>Angebot</span><span class="price">Preis</span></div></div>

  <footer class="abs site-footer"></footer>
  <div class="abs footer-col" style="left:79px"><h4>Sitemap</h4>Home<br>Immobilien Kaufen<br>Immobilien Verkaufen</div>
  <div class="abs footer-col" style="left:285px"><h4>Kontakt</h4>Jonas Beispiel<br>Lindenweg 4<br>12345 Beispielstadt<br>Tel.: 01 23 45 67 89 0<br>jonas@wohnraum-kontor.example</div>
  <div class="abs footer-col" style="left:490px"><h4>Impressum</h4>Jonas Beispiel<br>Lindenweg 4<br>12345 Beispielstadt<br>Tel.: 01 23 45 67 89 0</div>
  <div class="abs footer-col" style="left:695px"><h4>AGB</h4></div>
</body>
</html>
```